Spanish Student Needs a Cover for his PhD Dissertation

Hi everyone :) So, I'm a Corneal surgeon currently finishing my PhD, with a dissertation focused on the evaluation of quality of life in patients affected by a disease called Keratoconus. Just so you know, Keratoconus is a condition in which the cornea (the frontal part of the way) gets thin and bulgy and it decreases vision. What I did during my PhD was designing a questionnaire for evaluating quality of life in this kind of patients.
I need to design a hard cover for my dissertation, which is 200 sheets long. I like kind of minimalistic and geometric designs but I am totally open to suggestions. What needs to be in the cover is the name of the dissertation "Diseño, desarrollo y validación de una encuesta para evaluar el compromiso visual y emocional subjetivos en pacientes con Queratocono" and my name, "Iñigo Tarrasco". The other thing that needs to go there is the logo of my university (Universidad de Montebrisa). Aside from that, anything else is up to the designer. It would be important to use the kind of "red" color I am using in the dissertation. I am attaching the frontal page of my dissertation so you know what kind of design and colors I am using.
In the back part, of the cover, there should be this small inscription: "Iñigo Tarrasco, MD, es un Oftalmólogo Subespecialista en Cirugía Refractiva de la Universidad Serrana Metropolitana (Colombia) y la Universidad de Montebrisa (España). Actualmente se desempeña como miembro del Departamento de Córnea y Cirugía Refractiva de la Clínica de Oftalmología Vallealto y como director de su propia compañía de emprendimiento médico Silver Heron Surgical". Please leave a space to place my picture; I will have it taken this week so I don't have it right now, you can just leave the blank spot and I will include it later
The size of the pages is standard "letter" size.
Thanks a lot!

Target Market(s)

PhD Scholars

Font styles to use
Serif

Requirements
Must have
• The "red" color I use on my font. It must be formal but "young".
Nice to have
• I like to keep the design clean, kind of "formal with a young" touch so to speak. I really like gray colors, so it would be nice to have broad areas of gray. I love geometrical designs.
I have uploaded a very early version a friend of mine made (it even had a different title); this can be a starting point for you to work on, but I am more than open to suggestions and new ideas.
Should not have
• Please don't use my whole name, Iñigo Tarrasco is fine. I don't like ALL CAPITALS.

```html
<!DOCTYPE html>
<html lang="es">
<head>
<meta charset="utf-8">
<title>Cubierta de tesis doctoral – Iñigo Tarrasco</title>
<link rel="stylesheet" href="https://fonts.googleapis.com/css2?family=Libre+Baskerville&family=Source+Serif+4:wght@400;700&display=swap">
<style>
  :root {
    --canvas: #d9d9d9;
    --crimson: #a82239;
    --ink: #2b2b2b;
    --paper: #ffffff;
    --placeholder: #e4e4e6;
    --placeholder-text: #b3b3b8;
    --muted: #3a3a3a;
  }
  * { margin: 0; padding: 0; box-sizing: border-box; }
  html, body { width: 972px; height: 1200px; overflow: hidden; background: var(--canvas); }
  .spread {
    position: relative;
    width: 972px; height: 1200px;
  }
  .cover-page {
    position: absolute;
    top: 308px;
    width: 450px; height: 584px;
    background: var(--crimson);
    overflow: hidden;
  }
  .back-cover { left: 24px; }
  .front-cover { left: 498px; }
  .cover-art { position: absolute; inset: 0; width: 450px; height: 584px; }

  /* Back cover */
  .portrait-slot {
    position: absolute; left: 168px; top: 100px;
    width: 115px; height: 140px;
    background: var(--placeholder);
    display: flex; align-items: center; justify-content: center;
    font-family: Arial, Helvetica, sans-serif; font-size: 19px;
    color: var(--placeholder-text); letter-spacing: .5px;
  }
  .author-bio, .committee {
    position: absolute; left: 40px; width: 370px;
    text-align: center; color: var(--paper);
    font-family: "Source Serif 4", Georgia, serif;
  }
  .author-bio { top: 268px; font-size: 11.6px; line-height: 15.6px; }
  .author-bio strong { font-weight: 700; }
  .committee { top: 410px; font-size: 12.6px; line-height: 17px; }
  .committee .role { font-weight: 700; }
  .committee .member { margin-bottom: 8px; }

  /* Front cover */
  .affiliations {
    position: absolute; top: 22px; left: 110px; width: 260px;
    display: flex; justify-content: space-between; align-items: center;
    font-family: "Source Serif 4", Georgia, serif; font-weight: 700;
  }
  .affiliation { display: flex; align-items: center; gap: 4px; }
  .university-mark { font-size: 8px; color: var(--crimson); }
  .university-mark::before {
    content: ""; width: 22px; height: 22px; border-radius: 50%;
    background: var(--crimson); display: inline-block;
  }
  .school-mark { font-size: 12px; color: var(--ink); }
  .school-mark::before {
    content: ""; width: 14px; height: 14px;
    background: var(--crimson); display: inline-block;
  }
  .programme {
    position: absolute; top: 79px; left: 95px; width: 300px;
    text-align: center;
    font-family: "Source Serif 4", Georgia, serif;
    font-size: 9.2px; line-height: 12px;
  }
  .programme .institution { color: var(--crimson); font-weight: 700; }
  .programme .degree { color: var(--muted); }
  .thesis-title {
    position: absolute; top: 412px; left: 35px; width: 270px;
    font-family: "Libre Baskerville", Georgia, serif;
    font-size: 14.6px; line-height: 18.3px; color: var(--paper);
    font-weight: 400; letter-spacing: .2px;
  }
  .author-name {
    position: absolute; top: 530px; left: 36px;
    padding-left: 8px; height: 54px;
    border-left: 1.5px solid var(--paper);
    font-family: "Libre Baskerville", Georgia, serif;
    font-size: 23px; line-height: 44px; color: var(--paper);
    letter-spacing: .5px; font-weight: 400;
  }
</style>
</head>
<body>
<main class="spread">

  <section class="cover-page back-cover" aria-label="Contraportada">
    <div class="portrait-slot" aria-label="Espacio para la fotografía del autor">IMAGE</div>
    <p class="author-bio">
      <strong>Iñigo Tarrasco, MD,</strong> es un Oftalmólogo Subespecialista en Cirugía Refractiva de la Universidad Serrana Metropolitana (Colombia) y la Universidad de Montebrisa (España). Actualmente se desempeña como miembro del Departamento de Córnea y Cirugía Refractiva de la Clínica de Oftalmología Vallealto y como director de su propia compañía de emprendimiento médico Silver Heron Surgical".
    </p>
    <div class="committee">
      <p class="role">DIRECTOR:</p>
      <p class="member">Dr. Andrés Luis Ferrada Olmo</p>
      <p class="role">TUTOR:</p>
      <p class="member">Dr. Julián Tomás Berrocal Sanmartín</p>
    </div>
  </section>

  <section class="cover-page front-cover" aria-label="Portada">
    <svg class="cover-art" viewBox="0 0 443 575" preserveAspectRatio="none" aria-hidden="false">
      <defs>
        <linearGradient id="eye-tones" x1="0" y1="0" x2="1" y2="1">
          <stop offset="0" stop-color="#8a6a55"/>
          <stop offset=".45" stop-color="#c79a7c"/>
          <stop offset="1" stop-color="#e2bfa3"/>
        </linearGradient>
      </defs>
      <rect class="field-crimson" width="443" height="575" fill="var(--crimson)"/>
      <polygon class="field-white" points="35,0 443,0 443,400 300,400" fill="var(--paper)"/>
      <polygon class="accent-triangle" points="228,127 305,127 260,180" fill="var(--ink)"/>
      <g role="img" aria-label="Fotografía en primer plano de un ojo humano con pestañas">
        <polygon class="eye-photo" points="245,127 27,397 417,397" fill="url(#eye-tones)"/>
      </g>
      <polygon class="corner-block" points="288,405 443,405 443,575 395,575" fill="var(--ink)"/>
      <line class="corner-rule" x1="284" y1="405" x2="390" y2="575" stroke="var(--paper)" stroke-width="2"/>
      <polygon class="corner-notch" points="346,410 420,410 383,467" fill="var(--paper)"/>
    </svg>

    <div class="affiliations">
      <span class="affiliation university-mark">Universidad de Montebrisa</span>
      <span class="affiliation school-mark">EDUMB</span>
    </div>
    <div class="programme">
      <p class="institution">Universidad de Montebrisa</p>
      <p class="institution">Instituto Universitario de Oftalmociencia Aplicada</p>
      <p class="degree">Programa de Doctorado en Ciencias de la Visión</p>
    </div>

    <h1 class="thesis-title">Diseño, Desarrollo Y Validación De Una Encuesta Para Evaluar El Compromiso Visual Y Emocional Subjetivos En Pacientes Con Queratocono</h1>
    <p class="author-name">Iñigo&nbsp; Tarrasco</p>
  </section>

</main>
</body>
</html>
```